依頼詳細
A社より添付の案を頂いているのですが、①グループ会社である安心感親近感をアピールしたい②メリット1のA社専用のプランを他のメリットよりも強調したいと思い、依頼をさせて頂く事となりました。
注意点、会社案内欄の箇所は空白でお願い致します。
社名を変更して今後活用したいので、パワーポイントでの納品をお願い致します。
記載項目
株式会社ZAT/03-4817-2935/https://www.za-t.jp/
サイズ
A4
ページ数
片面
希望イメージ
シンプル 複雑
単色 カラフル
暗い 明るい
日常 高級
遊び心 厳粛
未来的 伝統的
女性的 男性的
希望する色
納品ファイル
補足説明
■ 選んだ理由

社員の選定を元に選ばせて頂きました。親近感があるという意見が多かったです。

■ 提案者全員のお礼・コメント

締め切りが近い中多数のご応募頂きありがとうございます。またご機会ありましたら宜しくお願い致します。

```html
<!DOCTYPE html>
<html lang="ja">
<head>
<meta charset="UTF-8">
<title>火災保険のご案内</title>
<link href="https://fonts.googleapis.com/css2?family=Noto+Sans+JP:wght@400;500;700;900&display=swap" rel="stylesheet">
<style>
  :root {
    --sky-top: #dcecf7;
    --sky-bottom: #b9d8ee;
    --navy: #1f3a5a;
    --ink: #333d47;
    --teal: #2b9aa3;
    --orange: #ef8a3c;
    --green: #8dc445;
    --red: #e2382c;
    --white: #ffffff;
    --panel: rgba(255,255,255,0.94);
  }
  * { box-sizing: border-box; margin: 0; padding: 0; }
  html, body { width: 839px; height: 1200px; overflow: hidden; }
  body {
    font-family: "Noto Sans JP", sans-serif;
    color: var(--ink);
    background: linear-gradient(180deg, var(--sky-top) 0%, #eaf4fb 30%, var(--sky-bottom) 100%);
    position: relative;
  }
  .abs { position: absolute; }
  .issue-date { top: 30px; right: 34px; font-size: 13px; color: var(--navy); }
  .house-photo {
    left: 34px; top: 66px; width: 142px; height: 104px;
    background: linear-gradient(160deg, #f3f6f8 0%, #c9d6df 55%, #8ea3b3 100%);
    border: 3px solid var(--white);
  }
  .headline {
    left: 196px; top: 72px; font-size: 34px; font-weight: 900;
    line-height: 1.25; color: var(--navy);
  }
  .intro { left: 196px; top: 170px; font-size: 17px; font-weight: 500; color: var(--navy); }
  .lead-band {
    left: 34px; top: 206px; width: 772px; height: 40px;
    background: rgba(255,255,255,0.85);
    display: flex; align-items: center; justify-content: center;
    font-size: 21px; font-weight: 700; color: var(--teal); letter-spacing: 1px;
  }
  .merit-label {
    font-size: 13px; font-style: italic; font-weight: 700; color: var(--white);
    letter-spacing: 1px; line-height: 1.4;
  }
  .merit-label b { font-size: 18px; }
  .head { padding: 6px 16px; color: var(--white); }
  .head-title { font-size: 19px; font-weight: 700; line-height: 1.3; margin-top: 2px; }
  .head-orange { background: var(--orange); }
  .head-green { background: var(--green); }
  .body-box {
    background: var(--panel); padding: 16px 18px;
    font-size: 16px; line-height: 1.75;
  }
  .plan-chip {
    display: inline-block; background: var(--white); color: var(--ink);
    padding: 6px 12px; font-size: 21px; font-weight: 900; line-height: 1.4;
    margin-top: 10px;
  }
  .plan-chip span { color: var(--orange); border-bottom: 3px solid var(--orange); }
  .price-box {
    left: 420px; top: 280px; width: 386px; height: 138px;
    background: var(--white); padding: 0 22px;
    display: flex; flex-direction: column; justify-content: center;
    font-size: 21px; font-weight: 700; line-height: 1.6;
  }
  .price-box .em { color: var(--red); border-bottom: 2px solid var(--red); }
  .price-box small { font-size: 17px; }
  .stat { color: var(--red); font-weight: 700; font-size: 18px; }
  .meeting-photo {
    left: 620px; top: 708px; width: 186px; height: 150px;
    background: linear-gradient(135deg, #f4f1ec 0%, #d8d0c4 50%, #8b8178 100%);
  }
  .notes { left: 34px; top: 1022px; width: 772px; font-size: 13px; line-height: 1.65; color: var(--navy); }
  .contact-pill {
    left: 34px; top: 1094px; width: 126px; height: 28px; border-radius: 14px;
    background: var(--white); color: var(--navy); font-size: 14px;
    display: flex; align-items: center; justify-content: center; gap: 6px;
  }
  .phone { left: 190px; top: 1082px; font-size: 34px; font-weight: 700; color: var(--navy); letter-spacing: 1px; line-height: 1.4; }
  .company { left: 34px; top: 1134px; font-size: 14px; line-height: 1.5; color: var(--navy); }
</style>
</head>
<body>
  <div class="abs issue-date">2021年1月以降保険開始期間</div>
  <div class="abs house-photo" role="img" aria-label="白い外壁の新築住宅の写真"></div>
  <h1 class="abs headline">A住宅会社の<br>住宅購入されるお客さまへ</h1>
  <p class="abs intro">A住宅会社より下記提携代理店をご紹介します。</p>
  <div class="abs lead-band">サンプル株式会社より専門火災保険のご案内です。</div>

  <div class="abs head head-orange" style="left:34px;top:280px;width:386px;height:138px;padding-top:12px;">
    <div class="merit-label">メリット<b>01</b></div>
    <div class="plan-chip">A住宅会社オーナー様<br><span>専用プラン適用！</span></div>
  </div>
  <div class="abs price-box">
    <div><span class="em">割安な保険料</span><small>（地震保険は除く）</small></div>
    <div>でご契約いただけます。</div>
  </div>

  <div class="abs head head-green" style="left:34px;top:426px;width:382px;height:84px;">
    <div class="merit-label">メリット<b>02</b></div>
    <div class="head-title">ご契約時お建物資料等の<br>ご提出不要！</div>
  </div>
  <div class="abs body-box" style="left:34px;top:510px;width:382px;height:190px;">
    A住宅会社と<br>サンプル株式会社の間で<br>直接やりとりいたします。
  </div>

  <div class="abs head head-green" style="left:424px;top:426px;width:382px;height:84px;">
    <div class="merit-label">メリット<b>03</b></div>
    <div class="head-title">サンプル株式会社は<br>火災保険専門代理店</div>
  </div>
  <div class="abs body-box" style="left:424px;top:510px;width:382px;height:190px;font-size:15px;">
    2019年度お取扱実績　<span class="stat">約3,500件</span><br>
    2020年8月時点保有契約件数 <span class="stat">約28,000件</span><br>
    火災保険専門ですのでお客様に<br>わかりやすくご案内させて頂きます。
  </div>

  <div class="abs head head-green" style="left:34px;top:708px;width:382px;height:82px;">
    <div class="merit-label">メリット<b>04</b></div>
    <div class="head-title">土日祝日も<br>ご案内いたします！</div>
  </div>
  <div class="abs body-box" style="left:34px;top:790px;width:382px;height:218px;">
    お客様のご都合の良い<br>日時にご案内させて<br>いただきます。
  </div>

  <div class="abs head head-green" style="left:424px;top:708px;width:196px;height:82px;">
    <div class="merit-label">メリット<b>05</b></div>
    <div class="head-title">スピーディーな<br>お申込み手続き！</div>
  </div>
  <div class="abs body-box" style="left:424px;top:790px;width:382px;height:218px;">
    最短で当日から<br>補償開始のお手続きが<br>可能です。
  </div>
  <div class="abs meeting-photo" role="img" aria-label="書類を前に打ち合わせをする場面の写真"></div>

  <div class="abs notes">
    こちらに注意点などを記載ください。こちらに注意点などを記載ください。こちらに注意点などを記載ください。<br>
    こちらに注意点などを記載ください。こちらに注意点などを記載ください。こちらに注意点などを記載ください。<br>
    こちらに注意点などを記載ください。
  </div>

  <div class="abs contact-pill">
    <svg width="14" height="14" viewBox="0 0 24 24" aria-hidden="true"><path fill="#1f3a5a" d="M6.6 10.8a15.1 15.1 0 0 0 6.6 6.6l2.2-2.2a1 1 0 0 1 1-.25 11.4 11.4 0 0 0 3.6.6 1 1 0 0 1 1 1V20a1 1 0 0 1-1 1A17 17 0 0 1 3 4a1 1 0 0 1 1-1h3.5a1 1 0 0 1 1 1c0 1.25.2 2.45.6 3.6a1 1 0 0 1-.25 1z"/></svg>
    お問い合わせ
  </div>
  <div class="abs phone">045-210-7783</div>
  <div class="abs company">
    サンプル株式会社<br>
    〒150-0042　東京都渋谷区＊＊＊＊<br>
    必要な情報をご記載ください。
  </div>
</body>
</html>
```